LOCAL TAXI SERVICE NEEDS A BANNER AD DESIGN

NEED BANNER AD DESIGN FOR TAXI SERVICE IN NJ. WE PROVIDE LOCAL AND LONG DISTANCE TRANSPORTATION. OUR MAIN BASE OF CUSTOMER GO TO THE MAJOR AIRPORTS IN THE TRI STATE AREA. I WANT TO OFFER A SPECIAL GOING TO DALMORE AIRPORT OF $35.00 WITH A COUPON CODE OF CP 12. THIS BANNER AD WILL BE USED FOR MY CHIRPLANE PAGE

Target Market(s)

PEOPLE WHO TRAVEL A LOT

Industry/Entity Type

Taxi

Font styles to use
Serif
Sans Serif

Colors
0792cd
0255a3
33a6d7
85cae6
cee9f5
ecf7fb
ffffff

Requirements
Must have
• MY COMPANY NAME: MAVIN'S TAXI

```html
<!DOCTYPE html>
<html lang="en">
<head>
<meta charset="utf-8">
<title>Mavin's Taxi – $35 to Dalmore Airport</title>
<link rel="stylesheet" href="https://fonts.googleapis.com/css2?family=Montserrat:wght@300;400;600&display=swap">
<style>
  :root {
    --brand-blue: #0792cd;
    --deep-blue: #0255a3;
    --mid-blue: #33a6d7;
    --soft-blue: #85cae6;
    --pale-blue: #cee9f5;
    --mist: #ecf7fb;
    --white: #ffffff;
    --price-ink: #3d5a6e;
  }
  * { margin: 0; padding: 0; box-sizing: border-box; }
  html, body { width: 1200px; height: 1000px; overflow: hidden; background: var(--brand-blue); }
  .banner {
    position: relative;
    width: 1200px;
    height: 1000px;
    overflow: hidden;
    background: var(--brand-blue);
    font-family: "Montserrat", sans-serif;
    color: var(--white);
  }
  .price-arrows { position: absolute; left: 0; top: 0; }
  .price {
    position: absolute;
    left: 289px;
    top: 194px;
    font-size: 44px;
    font-weight: 600;
    line-height: 56px;
    color: var(--price-ink);
    white-space: nowrap;
  }
  .destination {
    position: absolute;
    left: 658px;
    top: 168px;
    font-size: 46px;
    font-weight: 600;
    line-height: 60px;
    white-space: nowrap;
  }
  .vehicle-art {
    position: absolute;
    left: 36px;
    top: 425px;
    width: 656px;
    height: 365px;
    border-radius: 140px 160px 60px 60px;
    background: linear-gradient(180deg, var(--pale-blue) 0%, var(--soft-blue) 100%);
    opacity: 0.85;
  }
  .promo {
    position: absolute;
    left: 748px;
    top: 548px;
    width: 388px;
    height: 114px;
    background: var(--white);
    padding: 14px;
  }
  .promo-frame {
    width: 100%;
    height: 100%;
    border: 1.5px solid var(--brand-blue);
    display: flex;
    align-items: center;
    justify-content: center;
    color: var(--brand-blue);
    font-size: 38px;
    font-weight: 600;
    white-space: nowrap;
  }
  .brand {
    position: absolute;
    left: 733px;
    top: 891px;
    height: 77px;
    display: flex;
    align-items: center;
    white-space: nowrap;
  }
  .brand-mark {
    flex: none;
    width: 77px;
    height: 77px;
    border: 2px solid var(--white);
  }
  .brand-name {
    margin-left: 14px;
    font-size: 40px;
    font-weight: 300;
    letter-spacing: 1px;
    line-height: 1;
    white-space: nowrap;
  }
</style>
</head>
<body>
<main class="banner">
  <svg class="price-arrows" width="1200" height="1000" viewBox="0 0 1200 1000" aria-hidden="true">
    <polygon points="258,138 335,138 268,221 335,305 258,305 192,221" fill="#ffffff" opacity="0.35"/>
    <polygon points="298,172 432,172 432,271 298,271 230,221" fill="#ffffff" opacity="0.4"/>
    <polygon points="452,172 492,172 448,221 492,271 452,271 408,221" fill="#ffffff" opacity="0.4"/>
    <polygon points="512,172 548,172 508,221 548,271 512,271 472,221" fill="#ffffff" opacity="0.3"/>
    <polygon points="566,172 590,172 554,221 590,271 566,271 528,221" fill="#ffffff" opacity="0.2"/>
  </svg>
  <div class="price">$35</div>
  <h1 class="destination">TO<br>DALMORE AIRPORT</h1>
  <div class="vehicle-art" role="img" aria-label="Line illustration of a compact crossover car, three-quarter front view"></div>
  <div class="promo"><div class="promo-frame">PROMO: CP12</div></div>
  <div class="brand">
    <span class="brand-mark"></span>
    <span class="brand-name">MAVIN’S TAXI</span>
  </div>
</main>
</body>
</html>
```